Business Card Design

Certified KFL Instructor. Self defense instruction. Ladies classes available. Semi automatic and revolver

Industry/Entity Type

Defense

```html
<!DOCTYPE html>
<html lang="en">
<head>
<meta charset="utf-8">
<title>Business Card</title>
<link rel="stylesheet" href="https://fonts.googleapis.com/css2?family=Josefin+Sans:wght@400;600&display=swap">
<style>
  :root {
    --page-bg: #ffffff;
    --frame-yellow: #f7fa6a;
    --card-glow: #1c34ff;
    --card-mid: #0a1ee0;
    --card-edge: #000fb8;
    --emblem-light: #1a2cf0;
    --emblem-dark: #0b1bd8;
    --text-white: #ffffff;
    --text-soft: #dfe4ff;
  }

  html, body {
    margin: 0;
    padding: 0;
    width: 1200px;
    height: 702px;
    overflow: hidden;
    background: var(--page-bg);
  }

  .card {
    position: absolute;
    left: 48px;
    top: 46px;
    width: 1111px;
    height: 613px;
    box-sizing: border-box;
    border: 10px solid var(--frame-yellow);
    border-radius: 20px;
    background: var(--frame-yellow);
  }

  .card-face {
    position: absolute;
    inset: 0;
    border-radius: 10px;
    overflow: hidden;
    background: radial-gradient(ellipse 62% 68% at 51% 50%,
      var(--card-glow) 0%,
      var(--card-mid) 45%,
      var(--card-edge) 100%);
    font-family: "Josefin Sans", sans-serif;
    color: var(--text-white);
  }

  .emblem {
    position: absolute;
    left: 506px;
    top: 77px;
    width: 125px;
    height: 143px;
    border-radius: 14px;
    background: radial-gradient(ellipse at 50% 45%,
      var(--emblem-light) 0%,
      var(--emblem-dark) 100%);
  }

  .holder-name {
    position: absolute;
    left: 0;
    right: 0;
    top: 224px;
    margin: 0;
    text-align: center;
    font-size: 50px;
    font-weight: 400;
    font-variant: small-caps;
    letter-spacing: 4px;
    line-height: 1;
  }

  .contact-list {
    position: absolute;
    left: 333px;
    top: 283px;
    margin: 0;
    padding: 0;
    list-style: none;
    font-size: 31px;
    font-variant: small-caps;
    letter-spacing: 2px;
    line-height: 41.5px;
    white-space: nowrap;
  }

  .contact-label {
    font-weight: 600;
  }

  .services {
    position: absolute;
    left: 0;
    right: 0;
    top: 472px;
    margin: 0;
    text-align: center;
    font-variant: small-caps;
    letter-spacing: 2px;
    white-space: nowrap;
  }

  .services-title {
    display: block;
    font-size: 30px;
    line-height: 38px;
    font-weight: 600;
  }

  .services-line {
    display: block;
    font-size: 23px;
    line-height: 32px;
    color: var(--text-soft);
  }
</style>
</head>
<body>
  <div class="card">
    <div class="card-face">
      <div class="emblem" role="img" aria-label="Fleur-de-lis emblem in a slightly lighter blue"></div>
      <h1 class="holder-name">Jordan Vale</h1>
      <ul class="contact-list">
        <li class="contact-address"><span class="contact-label">Address:</span> 214 Ridge Road, Millbrook</li>
        <li class="contact-email"><span class="contact-label">Email:</span> jordan@valedefense.com</li>
        <li class="contact-phone"><span class="contact-label">Phone:</span> (555) 014-2290</li>
        <li class="contact-website"><span class="contact-label">Website:</span> valedefense.com</li>
      </ul>
      <p class="services">
        <span class="services-title">Certified KFL Instructor</span>
        <span class="services-line">Self Defense Instruction · Ladies Classes Available</span>
        <span class="services-line">Semi Automatic &amp; Revolver</span>
      </p>
    </div>
  </div>
</body>
</html>
```